Restaurant menu design

I need a menu for a restaurant in Spain.
It has to be bohemian but modern. We need something romantic and elegant.
The restaurant is elegant with good food and an excellent reputation. It is also modern at the same time.
The restaurant is superbly decorated and very chick so we need something "class" to fit in with the surroundings.
The size of the document must be 325 mm in high and 245 mm as a maximum and preferably made in indesign.

Reason: Thank you all for your designs.
So far all your designs are ok but it isn´t what we are looking for. Most of the designs are too loaded, too many colors and too much decoration.

Target Market(s)

Adults of various age groups and different nationalities mostly European.

Industry/Entity Type

Restaurant

Requirements
Must have
• The menu must have two interior pages with the text as in the document attached.It must be easily legible.
Nice to have
• See what kind of menus they use in important restaurants in places like Paris, see what designs are in trend, but Not necessarily doing the same style if it doesn’t fit in with the description above.
Should not have
• Nothing old fashioned.

```html
<!DOCTYPE html>
<html lang="en">
<head>
<meta charset="utf-8">
<title>la Velada — Menu Cover</title>
<link rel="stylesheet" href="https://fonts.googleapis.com/css2?family=Cormorant+Garamond:wght@500&display=swap">
<style>
  :root {
    --night: #231f20;
    --rose-line: #8c5a7c;
    --rose-frame: #b26a98;
    --pearl: #f3f2f3;
    --pearl-edge: #dcdadc;
    --cream-glow: #fbfbe6;
    --cream-soft: #f0f0ee;
    --ink: #231f20;
  }
  html, body {
    margin: 0;
    padding: 0;
    overflow: hidden;
    background: var(--night);
  }
  .menu-cover {
    position: relative;
    width: 905px;
    height: 1200px;
    background: var(--night);
    overflow: hidden;
  }
  .menu-cover svg {
    position: absolute;
    inset: 0;
    width: 905px;
    height: 1200px;
  }
  .outer-frame {
    fill: none;
    stroke: var(--rose-line);
    stroke-width: 1.2;
  }
  .emblem-plate {
    fill: var(--pearl);
    stroke: var(--rose-frame);
    stroke-width: 1.4;
  }
  .emblem-bevel {
    stroke: var(--pearl-edge);
    stroke-width: 1;
  }
  .emblem-field {
    fill: url(#creamGlow);
    stroke: var(--rose-frame);
    stroke-width: 1.2;
  }
  .brand-name {
    font-family: "Cormorant Garamond", Georgia, serif;
    font-weight: 500;
    font-size: 27px;
    fill: var(--ink);
    letter-spacing: 0.5px;
  }
</style>
</head>
<body>
  <main class="menu-cover">
    <svg viewBox="0 0 905 1200" xmlns="http://www.w3.org/2000/svg">
      <defs>
        <radialGradient id="creamGlow" cx="50%" cy="50%" r="55%">
          <stop offset="0%" stop-color="var(--cream-glow)"/>
          <stop offset="100%" stop-color="var(--cream-soft)"/>
        </radialGradient>
      </defs>

      <polygon class="outer-frame" points="452,208 842,599 452,989 61,599"/>

      <g class="cover-emblem">
        <polygon class="emblem-plate" points="453,453 600,599 453,746 307,599"/>
        <line class="emblem-bevel" x1="453" y1="453" x2="453" y2="501"/>
        <line class="emblem-bevel" x1="600" y1="599" x2="552" y2="599"/>
        <line class="emblem-bevel" x1="453" y1="746" x2="453" y2="697"/>
        <line class="emblem-bevel" x1="307" y1="599" x2="355" y2="599"/>
        <polygon class="emblem-field" points="453,501 552,599 453,697 355,599"/>
        <text class="brand-name" x="453" y="608" text-anchor="middle">la Velada</text>
      </g>
    </svg>
  </main>
</body>
</html>
```